New business stationairy

I need paper with header and footer and business cards.
I am a Ltd Company and my main field of expertise is QA/QC inspection in the Oil and Gas Industry. I will need all contact detail inserted and a footer with registration number and bank details etc

Business

```html
<!DOCTYPE html>
<html lang="en">
<head>
<meta charset="utf-8">
<title>Halloran Assurance Services Ltd – Letterhead</title>
<link href="https://fonts.googleapis.com/css2?family=Hind:wght@600&family=Cabin:wght@400&display=swap" rel="stylesheet">
<style>
  :root {
    --backdrop: #e9e9e9;
    --paper: #ffffff;
    --sidebar: #9cf7fb;
    --silhouette: #3f86e8;
    --brand-blue: #1c3fd8;
    --text-blue: #2f5fd6;
    --rule: #8f9cf0;
    --drop: #f2c21e;
    --reg-text: #ffffff;
  }
  html, body {
    margin: 0;
    padding: 0;
    width: 912px;
    height: 1200px;
    overflow: hidden;
    background: var(--backdrop);
  }
  .letterhead {
    position: absolute;
    left: 40px;
    top: 48px;
    width: 836px;
    height: 1092px;
    background: var(--paper);
    box-shadow: 0 2px 10px rgba(0,0,0,0.15);
  }
  .sidebar {
    position: absolute;
    left: 0;
    top: 0;
    width: 176px;
    height: 100%;
    background: var(--sidebar);
  }
  .sidebar__pumpjack {
    position: absolute;
    left: 28px;
    top: 10px;
    width: 142px;
    height: 152px;
    background: linear-gradient(180deg, rgba(63,134,232,0.55), var(--silhouette));
  }
  .sidebar__reg {
    position: absolute;
    top: 180px;
    width: 100%;
    text-align: center;
    font-family: "Cabin", sans-serif;
    font-size: 11px;
    color: var(--reg-text);
    letter-spacing: 0.2px;
  }
  .sidebar__refinery {
    position: absolute;
    left: 0;
    bottom: 10px;
    width: 176px;
    height: 108px;
    background: linear-gradient(180deg, rgba(63,134,232,0.35), var(--silhouette) 55%);
  }
  .header {
    position: absolute;
    left: 232px;
    top: 44px;
    right: 30px;
  }
  .header__name {
    margin: 0;
    font-family: "Hind", sans-serif;
    font-weight: 600;
    font-size: 32px;
    line-height: 1;
    color: var(--brand-blue);
    letter-spacing: 0.2px;
  }
  .header__address {
    margin: 10px 0 0;
    font-family: "Cabin", sans-serif;
    font-size: 16.5px;
    line-height: 21px;
    color: var(--text-blue);
  }
  .header__mark {
    position: absolute;
    right: 30px;
    top: 74px;
    width: 26px;
    height: 26px;
    border-radius: 50%;
    background: var(--drop);
  }
  .rule {
    position: absolute;
    height: 1.5px;
    background: var(--rule);
  }
  .rule--header { left: 190px; right: 4px; top: 156px; }
  .rule--footer { left: 176px; right: 24px; top: 1040px; }
  .footer {
    position: absolute;
    left: 208px;
    top: 1045px;
    font-family: "Cabin", sans-serif;
    font-size: 16px;
    color: var(--text-blue);
    white-space: nowrap;
  }
  .footer__sep { margin: 0 18px; }
</style>
</head>
<body>
  <main class="letterhead">
    <aside class="sidebar">
      <div class="sidebar__pumpjack" role="img" aria-label="Silhouette of an oil pump jack"></div>
      <div class="sidebar__reg">Reg. #4827160</div>
      <div class="sidebar__refinery" role="img" aria-label="Silhouette of a refinery skyline with smoking chimneys"></div>
    </aside>

    <header class="header">
      <h1 class="header__name">Halloran Assurance Services Ltd</h1>
      <p class="header__address">The Willows, Mill Lane, Ashby, Fernhurst,<br>Newbury, Berkshire RG14 7QP</p>
    </header>
    <span class="header__mark" aria-hidden="true"></span>
    <div class="rule rule--header"></div>

    <div class="rule rule--footer"></div>
    <footer class="footer">
      <span class="footer__email">email: inspect2204@example.co.uk</span><span class="footer__sep">•</span><span class="footer__phone">mobile: 07700 900418</span>
    </footer>
  </main>
</body>
</html>
```